New modern business card design

To design a brand new business card that's clean & modern in terms of layout.
I have attached our company logo and also basic information regarding what is needed on the card that also needs to be editable.

Target Market(s)

motor trade

Contact Information for Business Card

logo, name, title, tel, mob, email, address, www, all information is in the word.doc file

Requirements
Must have
• white background
Nice to have
• Nice clean font

```html
<!DOCTYPE html>
<html lang="en">
<head>
<meta charset="utf-8">
<title>Kestrel Extract Ltd Business Card</title>
<link href="https://fonts.googleapis.com/css2?family=Poppins:wght@300;400;500&display=swap" rel="stylesheet">
<style>
  :root {
    --canvas: #d6d6d6;
    --card: #ffffff;
    --brand-blue: #1d63b8;
    --text-grey: #4a4a4a;
    --muted-grey: #5a5a5a;
  }
  * { margin: 0; padding: 0; box-sizing: border-box; }
  html, body {
    width: 1200px; height: 1200px; overflow: hidden;
    background: var(--canvas);
    font-family: "Poppins", sans-serif;
  }
  .business-card {
    position: absolute;
    left: 50px; top: 270px;
    width: 1100px; height: 660px;
    background: var(--card);
  }
  .brand {
    position: absolute;
    left: 62px; top: 200px;
    display: flex; align-items: center; gap: 14px;
  }
  .brand-mark {
    width: 34px; height: 34px;
    background: var(--brand-blue);
  }
  .brand-name {
    font-weight: 500; font-size: 31px;
    color: var(--brand-blue);
    letter-spacing: 0.5px;
    white-space: nowrap;
  }
  .address {
    position: absolute;
    right: 37px; top: 128px;
    text-align: right;
    font-weight: 400; font-size: 31px; line-height: 43px;
    color: var(--text-grey);
    font-style: normal;
  }
  .person {
    position: absolute;
    left: 53px; top: 454px;
  }
  .person-name {
    font-weight: 400; font-size: 52px; line-height: 56px;
    color: var(--brand-blue);
  }
  .person-title {
    font-weight: 300; font-size: 29px; line-height: 40px;
    color: var(--muted-grey);
  }
  .contact-list {
    position: absolute;
    right: 32px; top: 380px;
    list-style: none;
  }
  .contact-item {
    display: flex; align-items: center; justify-content: flex-end;
    height: 50px;
    font-weight: 400; font-size: 30px;
    color: var(--text-grey);
  }
  .contact-icon {
    width: 34px; height: 34px; margin-left: 22px;
    flex: none;
  }
</style>
</head>
<body>
  <section class="business-card">
    <div class="brand">
      <span class="brand-mark"></span>
      <span class="brand-name">KESTREL EXTRACT LTD</span>
    </div>

    <address class="address">
      Carrow Lane<br>
      Ashbury, Westfield<br>
      WF12 8QT
    </address>

    <div class="person">
      <p class="person-name">Daniel Whitmore</p>
      <p class="person-title">General Manager</p>
    </div>

    <ul class="contact-list">
      <li class="contact-item">0161 555 0142
        <svg class="contact-icon" viewBox="0 0 24 24" aria-hidden="true">
          <path fill="#1d63b8" d="M6.6 3.5l2.6 3.2-1.6 2.1c1 2.2 2.9 4.1 5.2 5.2l2.1-1.6 3.2 2.6-1.3 3c-6.6.2-12.5-5.7-12.3-12.3z"/>
          <path fill="none" stroke="#1d63b8" stroke-width="1.6" stroke-linecap="round" d="M13.5 3.5a7 7 0 0 1 6.5 6.5M13.5 7a3.5 3.5 0 0 1 3.2 3.2"/>
        </svg>
      </li>
      <li class="contact-item">07700 900 418
        <svg class="contact-icon" viewBox="0 0 24 24" aria-hidden="true">
          <rect x="6.5" y="1.5" width="11" height="21" rx="2" fill="none" stroke="#1d63b8" stroke-width="1.8"/>
          <rect x="8.5" y="4" width="7" height="13" fill="#1d63b8" opacity=".15"/>
          <circle cx="12" cy="19.6" r="1" fill="#1d63b8"/>
        </svg>
      </li>
      <li class="contact-item">dwhitmore@kestrel-extract.co.uk
        <svg class="contact-icon" viewBox="0 0 24 24" aria-hidden="true">
          <rect x="2" y="6" width="20" height="13" rx="1.5" fill="#1d63b8"/>
          <path d="M2.5 7l9.5 6.5L21.5 7" fill="none" stroke="#fff" stroke-width="1.5"/>
        </svg>
      </li>
      <li class="contact-item">www.kestrel-extract.co.uk
        <svg class="contact-icon" viewBox="0 0 24 24" aria-hidden="true">
          <g fill="none" stroke="#1d63b8" stroke-width="1.2">
            <circle cx="12" cy="12" r="9.5"/>
            <ellipse cx="12" cy="12" rx="4.2" ry="9.5"/>
            <path d="M2.5 12h19M4 7h16M4 17h16M12 2.5v19"/>
          </g>
        </svg>
      </li>
    </ul>
  </section>
</body>
</html>
```